【依頼の目的/概要】
電子書籍(bookrie)の表紙デザインをお願いします。

【画像サイズ】※BRPより抜粋
表紙ファイルの理想的な寸法は2,560×1,600ピクセルです。
注:画像の寸法は10,000×10,000ピクセルです。

【タイトル】
資格試験 ゴールダッシュ・速習・楽々学習術

サブタイトル
通れる学び方

【著者】
行政書士 社会保険労務士
森川澄江

【本の内容】
行政書士試験の勉強を短期間で仕上げて、合格する勉強法を
書いた本です。

【デザイン要望】
特にこだわりません。
素敵なデザインの応募を楽しみにしています。
※次点、次々点の方への参加報酬を設定しました。

その他
必要な情報がありましたらお問い合わせください。

本を以下に添付します。
本文中にエクセルで作成した表を挿入します。

明るく見やすく、わかり易い表現が良かったです。

皆様お疲れ様でした。
T_okabe様には訂正を速攻して頂きありがとうございました。
最後まで迷いました。
皆様のご依頼が増えますことをご祈念申し上げます。

```html
<!DOCTYPE html>
<html lang="ja">
<head>
<meta charset="utf-8">
<title>資格試験 ゴールダッシュ・速習・楽々学習術</title>
<link rel="stylesheet" href="https://fonts.googleapis.com/css2?family=M+PLUS+1p:wght@500;800;900&family=Noto+Sans+JP:wght@500;700;900&display=swap">
<style>
  :root {
    --navy: #1d3766;
    --blue: #2b8fd6;
    --sky: #cfe6f7;
    --orange: #ef8a22;
    --paper: #f7f8f9;
    --white: #ffffff;
  }
  * { margin: 0; padding: 0; box-sizing: border-box; }
  html, body { width: 900px; height: 1200px; overflow: hidden; background: var(--paper); }
  .cover {
    position: relative; width: 900px; height: 1200px; overflow: hidden;
    background: var(--paper);
    font-family: "Noto Sans JP", sans-serif; color: var(--navy);
  }
  .rays { position: absolute; inset: 0; }
  .kicker {
    position: absolute; top: 26px; left: 0; width: 100%; text-align: center;
    font-family: "M PLUS 1p", sans-serif; font-weight: 900; font-size: 44px; line-height: 1;
    color: var(--navy); letter-spacing: 2px;
  }
  .kicker .slash { color: var(--navy); font-weight: 500; margin: 0 10px; }

  .figure {
    position: absolute; left: 330px; top: 600px; width: 300px; height: 600px;
    border-radius: 130px 130px 0 0;
    background: linear-gradient(180deg, #fde3c6 0%, #f6a55a 60%, #f08a24 100%);
    opacity: .85;
  }

  .title-bubble { position: absolute; left: 170px; top: 135px; width: 560px; height: 445px; }
  .title-bubble svg { position: absolute; inset: 0; overflow: visible; }
  .title-line {
    position: absolute; left: 0; width: 100%; text-align: center; display: block;
    font-family: "M PLUS 1p", sans-serif; font-weight: 900; line-height: 1; white-space: nowrap;
  }
  .title-line.exam { top: 42px; font-size: 114px; color: var(--navy); letter-spacing: 2px; }
  .title-line.fast { top: 186px; font-size: 66px; color: var(--blue); letter-spacing: 4px; }
  .title-line.method { top: 282px; font-size: 100px; color: var(--navy); }
  .title-line.method em {
    font-style: normal;
    background: linear-gradient(transparent 60%, var(--sky) 60%);
    padding: 0 6px;
  }

  .badge-days {
    position: absolute; left: 420px; top: 592px; width: 104px; height: 104px;
    border-radius: 50%; background: var(--orange); color: var(--white);
    display: flex; flex-direction: column; align-items: center; justify-content: center;
    font-weight: 900; line-height: 1.05;
  }
  .badge-days small { font-size: 18px; }
  .badge-days b { font-size: 32px; }

  .v { position: absolute; writing-mode: vertical-rl; font-weight: 900; line-height: 1; white-space: nowrap; }
  .v-promise { left: 176px; top: 600px; font-size: 43px; color: var(--navy); }
  .v-subtitle { left: 234px; top: 600px; font-size: 72px; color: var(--orange); }
  .v-pass { left: 318px; top: 600px; font-size: 43px; color: var(--navy); }
  .v-pass .hl { background: var(--orange); color: var(--white); padding: 4px 0; }
  .v-profile { left: 664px; top: 596px; font-size: 48px; color: var(--navy); }
  .v-profile .hl { background: var(--orange); color: var(--white); padding: 6px 4px; font-size: 56px; }
  .v-profile .small { font-size: 40px; }
  .v-family {
    left: 736px; top: 556px; font-size: 58px; line-height: 1.1; color: var(--white);
    background: var(--orange); padding: 14px 10px; letter-spacing: 6px;
  }

  .author { position: absolute; left: 24px; top: 1062px; }
  .author .role { font-size: 20px; font-weight: 700; color: var(--navy); line-height: 1.2; }
  .author .name { font-size: 48px; font-weight: 900; color: var(--navy); letter-spacing: 4px; line-height: 1.2; margin-top: 4px; }

  .note-bar {
    position: absolute; left: 486px; top: 1112px; width: 396px; height: 58px;
    border-radius: 12px; background: var(--navy); color: var(--white);
    display: flex; align-items: center; justify-content: center;
    font-size: 22px; font-weight: 700; white-space: nowrap;
  }
</style>
</head>
<body>
<main class="cover">
  <svg class="rays" viewBox="0 0 900 1200" aria-hidden="true">
    <g stroke="var(--blue)" stroke-width="5" stroke-linecap="round">
      <line x1="60" y1="150" x2="20" y2="112"/>
      <line x1="58" y1="250" x2="12" y2="242"/>
      <line x1="86" y1="92" x2="56" y2="44"/>
      <line x1="840" y1="150" x2="880" y2="112"/>
      <line x1="842" y1="250" x2="888" y2="242"/>
      <line x1="814" y1="92" x2="844" y2="44"/>
    </g>
  </svg>

  <p class="kicker"><span class="slash">＼</span>ゴールダッシュ！<span class="slash">／</span></p>

  <div class="figure" role="img" aria-label="自信に満ちた女性のイラスト"></div>

  <div class="title-bubble">
    <svg viewBox="0 0 560 445" aria-hidden="true">
      <path d="M40 6 H520 Q554 6 554 40 V405 Q554 439 520 439 H300 L276 490 L256 439 H40 Q6 439 6 405 V40 Q6 6 40 6 Z"
            fill="var(--white)" stroke="var(--blue)" stroke-width="8" stroke-linejoin="round"/>
    </svg>
    <h1>
      <span class="title-line exam">資格試験</span>
      <span class="title-line fast">速習</span>
      <span class="title-line method"><em>楽々学習術</em></span>
    </h1>
  </div>

  <div class="badge-days"><small>たった</small><b>30日</b><small>で</small></div>

  <p class="v v-promise">この一冊で教えます。</p>
  <h2 class="v v-subtitle">通れる学び方</h2>
  <p class="v v-pass">行政書士に<span class="hl">一発合格</span>。</p>

  <p class="v v-profile"><span class="hl">高卒</span><span class="small">の</span>私が時短勉強</p>
  <p class="v v-family">専業主婦<br>子供4人</p>

  <div class="author">
    <p class="role">行政書士 社会保険労務士</p>
    <p class="name">森川澄江</p>
  </div>

  <p class="note-bar">合格ラインを把握、6割正解でOK?</p>
</main>
</body>
</html>
```